We are in search of a new business card design for our business. We have a Mexican Grocery Store called Tortilla Grove Market, we would like to see that some have mexican design, but we are open to any type of designs.

Phone: to be announced
Fax: to be announced

Address is:
2415 Calloway Blvd
Larkfield, MD 21099

```html
<!DOCTYPE html>
<html lang="en">
<head>
<meta charset="utf-8">
<title>Tortilla Grove Market – Business Card</title>
<link rel="stylesheet" href="https://fonts.googleapis.com/css2?family=Open+Sans:wght@400;700;800&display=swap">
<style>
  :root {
    --page-bg: #2b2b2b;
    --card-white: #ffffff;
    --panel-dark: #454545;
    --accent-red: #d42027;
    --accent-green: #2a8d3f;
    --accent-yellow: #fbb714;
    --name-gray: #3f3f3f;
    --text-light: #ffffff;
    --brand-red: #c8202a;
  }
  * { box-sizing: border-box; margin: 0; padding: 0; }
  html, body {
    width: 1200px; height: 1000px; overflow: hidden;
    background: var(--page-bg);
    font-family: "Open Sans", Arial, sans-serif;
  }
  .business-card {
    position: absolute; left: 160px; top: 265px;
    width: 880px; height: 470px;
    border-radius: 36px; overflow: hidden;
    background: var(--card-white);
    box-shadow: 0 18px 40px rgba(0,0,0,.45);
  }
  .identity {
    position: absolute; left: 0; top: 0; width: 415px; height: 100%;
  }
  .person-name {
    position: absolute; left: 95px; top: 150px;
    font-size: 36px; font-weight: 800; letter-spacing: .5px;
    color: var(--name-gray); line-height: 1;
  }
  .person-name .surname { color: var(--accent-yellow); }
  .person-role {
    position: absolute; left: 160px; top: 192px;
    font-size: 19px; font-weight: 700; color: var(--accent-red);
  }
  .brand-block {
    position: absolute; left: 60px; top: 270px; width: 300px;
    display: flex; align-items: center; gap: 14px;
  }
  .brand-dot {
    flex: none; width: 38px; height: 38px; border-radius: 50%;
    background: var(--accent-green);
  }
  .brand-name {
    font-size: 30px; font-weight: 800; line-height: 1.1;
    color: var(--brand-red);
  }
  .contact-list {
    position: absolute; left: 415px; top: 0; width: 465px; height: 100%;
    display: flex; flex-direction: column; gap: 9px;
    background: var(--card-white);
  }
  .contact-row { display: flex; flex: 1; }
  .contact-icon {
    width: 150px; display: flex; align-items: center; justify-content: center;
  }
  .contact-icon svg { width: 44px; height: 44px; fill: var(--text-light); }
  .row-address .contact-icon { background: var(--accent-red); }
  .row-phone .contact-icon { background: var(--accent-green); }
  .row-fax .contact-icon { background: var(--accent-yellow); }
  .contact-text {
    flex: 1; background: var(--panel-dark);
    display: flex; flex-direction: column; justify-content: center;
    padding-left: 40px;
    color: var(--text-light); font-size: 21px; line-height: 1.25;
  }
</style>
</head>
<body>
  <div class="business-card">
    <div class="identity">
      <h1 class="person-name">MARCO <span class="surname">RUELAS</span></h1>
      <p class="person-role">Founder</p>
      <div class="brand-block">
        <span class="brand-dot"></span>
        <span class="brand-name">Tortilla Grove Market</span>
      </div>
    </div>

    <div class="contact-list">
      <div class="contact-row row-address">
        <div class="contact-icon">
          <svg viewBox="0 0 24 24" aria-hidden="true"><path d="M12 3 2 12h3v8h5v-5h4v5h5v-8h3z"/></svg>
        </div>
        <div class="contact-text">
          <span>2415 Calloway Blvd</span>
          <span>Larkfield, MD 21099</span>
        </div>
      </div>
      <div class="contact-row row-phone">
        <div class="contact-icon">
          <svg viewBox="0 0 24 24" aria-hidden="true"><path d="M6.6 10.8a15.1 15.1 0 0 0 6.6 6.6l2.2-2.2c.3-.3.7-.4 1-.2 1.1.4 2.3.6 3.6.6.6 0 1 .4 1 1V20c0 .6-.4 1-1 1A17 17 0 0 1 3 4c0-.6.4-1 1-1h3.5c.6 0 1 .4 1 1 0 1.3.2 2.5.6 3.6.1.3 0 .7-.2 1z"/></svg>
        </div>
        <div class="contact-text"><span>410-555-0136</span></div>
      </div>
      <div class="contact-row row-fax">
        <div class="contact-icon">
          <svg viewBox="0 0 24 24" aria-hidden="true"><path d="M7 2h8l3 3v4H7zM4 10h16a2 2 0 0 1 2 2v6h-4v4H6v-4H2v-6a2 2 0 0 1 2-2zm4 6v4h8v-4z"/></svg>
        </div>
        <div class="contact-text"><span>410-555-0136</span></div>
      </div>
    </div>
  </div>
</body>
</html>
```